Web Design Project

We are a SaaS company that specializes in the thrift industry POS and inventory software. We want a clean and professional site that does NOT look like a template site.

*** A little more about our business -
We offer a SaaS (Software As A Service) for a Point Of Sale and inventory control product specifically for the Thrift / Second hand industry. The software allows them to process inventory, grade/rate it, create the barcoded tags. It the does the whole retail sale process. We also offer tie-ins to Pixelyard, Chirpnest and apple/droid mobile apps to support our customers thrift stores.

We need to in incorporate the look/feel and color scheme of our logo.

I would imagine possibly a HTML5 slideshow (3-5 slides) rotating on the home page showing screenshots, etc.

I am envisioning icons representing features of our product.

PLEASE ask questions, I am sure I have left out a ton.
Updates

Requirements
Must have
• I have attached a couple of our logo's with color options. It needs to flow with that.

I have also attached a screen shot of what I think might work. This DOESN'T suggest that is what I am looking for, just a sample.

I am thinking a home page and maybe one or two sub pages
***Update, I kind of like the following concept for one of the sub-pages
http://www.quotivex.example/estimate.html

There should also be a place to highlight Pixelyard and chirpnest.

It will be a bilingual / multilingual site, so take that into account
Should not have
• I don't want it to look like a template site. It should be clean and professional.

```html
<!DOCTYPE html>
<html lang="en">
<head>
<meta charset="utf-8">
<title>Secondloop — Track time, monitor expenses and invoice online</title>
<link href="https://fonts.googleapis.com/css2?family=Roboto+Condensed:wght@400;700&family=Arimo:wght@400;700&display=swap" rel="stylesheet">
<style>
:root{
  --ink-dark:#2e3237;
  --ink-darker:#26292d;
  --blue:#1b8fd2;
  --blue-deep:#0f5d92;
  --blue-light:#3fb3ea;
  --accent:#2aa7e6;
  --paper:#f3f3f3;
  --text:#4a4a4a;
  --title:#222;
  --footer:#333333;
  --footer-line:#444;
  --footer-text:#cfcfcf;
}
*{box-sizing:border-box;margin:0;padding:0}
html,body{width:1117px;height:1200px;overflow:hidden}
body{font-family:"Arimo",Arial,sans-serif;background:var(--paper);position:relative}
.cond{font-family:"Roboto Condensed","Arial Narrow",sans-serif}

/* header */
.site-header{position:absolute;left:0;top:0;width:1117px;height:95px;background:var(--ink-dark)}
.brand{position:absolute;left:141px;top:28px;display:flex;align-items:center;gap:10px;color:var(--blue-light);font:700 34px "Roboto Condensed",sans-serif;letter-spacing:.5px}
.brand-dot{width:36px;height:36px;border-radius:50%;background:var(--blue-light)}
.main-nav{position:absolute;left:528px;top:38px;display:flex;gap:22px;align-items:center}
.main-nav a{color:#fff;text-decoration:none;font:400 19px "Roboto Condensed",sans-serif}
.hatch{position:absolute;left:0;width:1117px;height:6px;background:repeating-linear-gradient(135deg,#1a1c1f 0 2px,#4a4e54 2px 4px)}

/* hero */
.hero{position:absolute;left:0;top:101px;width:1117px;height:312px;background:radial-gradient(ellipse at 40% 55%,#1fa6e8 0%,#148bcd 45%,#0d6aa6 100%)}
.hero-copy{position:absolute;left:143px;top:34px;color:#fff}
.hero-copy .lead{font:400 30px/1 "Roboto Condensed",sans-serif;color:#f3f7fa}
.hero-copy .strong{font:700 41px/1.1 "Roboto Condensed",sans-serif;color:#111;letter-spacing:-.5px;margin-top:6px}
.hero-copy .strong span{font-weight:400;font-size:29px;color:#fff}
.hero-copy .big{font:400 45px/1 "Roboto Condensed",sans-serif;margin-top:6px}
.cta{position:absolute;left:141px;top:243px;width:214px;height:45px;border-radius:6px;background:linear-gradient(#1d4f7c,#0c2e4e);box-shadow:0 3px 6px rgba(0,0,0,.4);color:#fff;font:400 20px "Roboto Condensed",sans-serif;display:flex;align-items:center;padding-left:24px;gap:36px}
.cta i{width:16px;height:16px;border-radius:50%;background:#2f9be2;display:inline-flex;align-items:center;justify-content:center}
.hero-visual{position:absolute;left:580px;top:14px;width:390px;height:296px;border-radius:6px;background:linear-gradient(160deg,#e9f2f8 0%,#c7dbe9 55%,#5fb3e0 100%);opacity:.92}

/* welcome */
.welcome{position:absolute;left:0;top:419px;width:1117px;height:132px;background:linear-gradient(#2f3338,#25282c)}
.welcome h2{position:absolute;left:148px;top:8px;color:#fff;font:400 33px "Roboto Condensed",sans-serif}
.welcome p{position:absolute;left:145px;top:49px;width:250px;color:#e6e6e6;font-size:10.5px;line-height:19px}
.slide-dots{position:absolute;left:735px;top:13px;display:flex;gap:3px}
.slide-dots span{width:11px;height:11px;border-radius:50%;background:#1a1a1a;box-shadow:inset 0 0 0 1px #555}
.slide-dots span.on{background:var(--accent)}
.testimonial{position:absolute;left:480px;top:51px;width:535px;text-align:center;font:400 21px/26px "Roboto Condensed",sans-serif;color:#fff}
.testimonial em{font-style:normal;color:var(--accent)}

/* tabs */
.feature-tabs{position:absolute;left:0;top:551px;width:1117px;height:73px;background:linear-gradient(#0e6aa8,#0a4d7e 70%,#083c63)}
.tab{position:absolute;top:7px;height:66px;text-align:center;color:#fff;font:400 17px "Roboto Condensed",sans-serif}
.tab svg{display:block;margin:2px auto 4px}
.tab.active{background:linear-gradient(#d8dadc,#fff 40%);color:#333}

/* features */
.features{position:absolute;left:0;top:624px;width:1117px;height:315px;background:var(--paper)}
.feature{position:absolute;width:250px}
.feature .icon{position:absolute;left:0;top:0;width:44px;height:44px}
.feature h3{position:absolute;left:59px;top:1px;font:700 12px "Arimo",sans-serif;color:var(--title);white-space:nowrap}
.feature p{position:absolute;left:59px;top:26px;width:216px;font-size:10.5px;line-height:19px;color:var(--text)}

/* footer */
.site-footer{position:absolute;left:0;top:939px;width:1117px;height:261px;background:var(--footer);color:var(--footer-text)}
.site-footer h4{font:400 19px "Roboto Condensed",sans-serif;color:#ddd;position:absolute}
.col-rule{position:absolute;top:16px;width:1px;height:175px;background:var(--footer-line)}
.footer-links{position:absolute;left:130px;top:50px;display:grid;grid-template-columns:88px 88px;column-gap:55px}
.footer-links a{display:block;color:#ddd;font-size:10.5px;text-decoration:none;height:30px;line-height:30px;border-bottom:1px solid #2a2a2a;box-shadow:0 1px 0 #3d3d3d}
.recommend{position:absolute;left:423px;top:62px;display:flex;gap:7px;align-items:flex-start}
.recommend .btn{border:1px solid #999;background:linear-gradient(#fafafa,#ddd);color:#333;font-size:9.5px;padding:3px 6px;border-radius:2px}
.recommend .count{color:#888;font-size:9px;line-height:13px}
.social-pill{position:absolute;left:797px;top:42px;width:152px;height:30px;border-radius:15px;background:#dcdcdc;display:flex;align-items:center;justify-content:space-around;padding:0 6px;font:700 8.5px "Arimo",sans-serif;color:#666}
.legal{position:absolute;left:780px;top:84px;width:185px;text-align:center;font-size:10.5px;line-height:16px;color:#eee}
.legal-links{position:absolute;left:780px;top:133px;width:185px;text-align:center;font-size:10.5px;line-height:28px;color:#ccc}
.legal-links a{color:#ccc}
.legal-links b a{font-weight:700}
</style>
</head>
<body>

<header class="site-header">
  <div class="brand"><span class="brand-dot"></span>secondloop</div>
  <nav class="main-nav">
    <svg width="14" height="13" viewBox="0 0 14 13" aria-label="Home"><path d="M7 0 0 6h2v7h4V9h2v4h4V6h2z" fill="#fff"/></svg>
    <a href="#">PRICING &amp; SIGNUP</a><a href="#">SERVICES</a><a href="#">TOUR</a><a href="#">AFFILIATE</a>
  </nav>
</header>
<div class="hatch" style="top:95px"></div>

<section class="hero">
  <div class="hero-copy">
    <div class="lead">The Easiest and fastest way to</div>
    <div class="strong">TRACK TIME, MONITOR<br>EXPENSES <span>and</span></div>
    <div class="big">INVOICE ONLINE</div>
  </div>
  <a class="cta">FIND OUT MORE <i><svg width="10" height="10" viewBox="0 0 10 10"><path d="M1 5h6M5 2l3 3-3 3" stroke="#fff" stroke-width="1.8" fill="none"/></svg></i></a>
  <div class="hero-visual" role="img" aria-label="Illustration of a sample invoice sheet surrounded by a calculator, hourglass, credit card, money bag and clouds"></div>
</section>
<div class="hatch" style="top:413px"></div>

<section class="welcome">
  <h2>WELCOME</h2>
  <p>Lorem ipsum dolor sit amet, consectetuer adipiscing elit, sed diam nonummy nibh euismod tincidunt ut laoreet dolore magna aliquam erat volutpat. Ut wisi enim ad minim veniam</p>
  <div class="slide-dots"><span class="on"></span><span></span><span></span></div>
  <div class="testimonial">What our users are saying after <em>using easy &amp; secure<br>Invoicing Solution Secondloop</em></div>
</section>

<nav class="feature-tabs">
  <div class="tab active" style="left:380px;width:98px">
    <svg width="22" height="28" viewBox="0 0 22 28"><g fill="#333"><rect x="2" y="4" width="18" height="3"/><rect x="2" y="11" width="12" height="3"/><rect x="2" y="18" width="18" height="3"/><rect x="2" y="25" width="8" height="3"/></g></svg>Dashboard</div>
  <div class="tab" style="left:500px;width:80px">
    <svg width="26" height="32" viewBox="0 0 26 32"><rect x="1" y="1" width="24" height="30" fill="#f2f2f2" stroke="#999"/><g stroke="#999"><path d="M5 8h16M5 13h16M5 18h16M5 23h16M10 8v15M16 8v15"/></g></svg>Invoices</div>
  <div class="tab" style="left:604px;width:80px">
    <svg width="26" height="34" viewBox="0 0 26 34"><rect x="1" y="3" width="24" height="30" fill="#f7f7f7" stroke="#999"/><g fill="#555"><circle cx="7" cy="4" r="2"/><circle cx="13" cy="4" r="2"/><circle cx="19" cy="4" r="2"/></g><g stroke="#888"><path d="M5 12h16M5 17h16M5 22h16M5 27h10"/></g></svg>Estimates</div>
  <div class="tab" style="left:715px;width:100px">
    <svg width="34" height="34" viewBox="0 0 34 34"><circle cx="17" cy="17" r="16" fill="#eee" stroke="#777" stroke-width="2"/><path d="M17 7v10l7 4" stroke="#333" stroke-width="2" fill="none"/></svg>Time Tracking</div>
  <div class="tab" style="left:845px;width:90px">
    <svg width="44" height="34" viewBox="0 0 44 34"><rect x="6" y="4" width="32" height="18" rx="2" fill="#bbb" transform="rotate(-12 22 13)"/><circle cx="15" cy="16" r="6" fill="#666"/><circle cx="27" cy="24" r="6" fill="#888"/></svg>Expenses</div>
</nav>

<section class="features">
  <article class="feature" style="left:146px;top:37px">
    <svg class="icon" viewBox="0 0 44 44"><rect x="1" y="1" width="42" height="42" rx="7" fill="#e6e6e6" stroke="#999"/><rect x="5" y="5" width="34" height="34" rx="5" fill="#2b2b2b"/><path d="M10 30a12 12 0 0 1 24 0" stroke="#ddd" stroke-width="2" fill="none"/><path d="M22 30l8-9" stroke="#e33" stroke-width="2.5"/></svg>
    <h3>CONNECTION</h3>
    <p>Lorem ipsum dolor sit amet, consectetuer adipiscing elit, sed diam nonummy nibh euismod tincidunt ut laoreet dolore magna aliquam erat volutpat. Ut wisi enim ad minim veniam.</p>
  </article>
  <article class="feature" style="left:439px;top:37px">
    <svg class="icon" viewBox="0 0 44 44"><rect x="1" y="1" width="42" height="42" rx="7" fill="#ee6a1e"/><path d="M22 34 9 21a7 7 0 0 1 13-8 7 7 0 0 1 13 8z" fill="#fff"/></svg>
    <h3>PERSONAL &nbsp;SUPPORT</h3>
    <p>Lorem ipsum dolor sit amet, consectetuer adipiscing elit, sed diam nonummy nibh euismod tincidunt ut laoreet dolore magna aliquam erat volutpat. Ut wisi enim ad minim veniam.</p>
  </article>
  <article class="feature" style="left:731px;top:37px">
    <svg class="icon" viewBox="0 0 44 44"><rect x="1" y="1" width="42" height="42" rx="6" fill="#6f7f95" stroke="#4b5666"/><rect x="7" y="7" width="30" height="30" rx="3" fill="#a9b4c3"/><circle cx="20" cy="22" r="7" fill="#e8ecf0" stroke="#555"/><rect x="32" y="15" width="3" height="14" fill="#555"/></svg>
    <h3>SECURITY &amp; RELIABILITY</h3>
    <p>Lorem ipsum dolor sit amet, consectetuer adipiscing elit, sed diam nonummy nibh euismod tincidunt ut laoreet dolore magna aliquam erat volutpat. Ut wisi enim ad minim veniam.</p>
  </article>
  <article class="feature" style="left:146px;top:175px">
    <svg class="icon" viewBox="0 0 44 44"><rect x="2" y="3" width="40" height="40" rx="7" fill="#eee" stroke="#888"/><circle cx="22" cy="19" r="12" fill="#d22"/><path d="M22 12v14M15 19h14" stroke="#fff" stroke-width="4"/><rect x="8" y="36" width="28" height="4" fill="#555"/></svg>
    <h3>DATA BACKUP &amp; REDUNDANCY</h3>
    <p>Lorem ipsum dolor sit amet, consectetuer adipiscing elit, sed diam nonummy nibh euismod tincidunt ut laoreet dolore magna aliquam erat volutpat. Ut wisi enim ad minim veniam.</p>
  </article>
  <article class="feature" style="left:439px;top:175px">
    <svg class="icon" viewBox="0 0 44 44"><rect x="1" y="1" width="42" height="42" rx="4" fill="#3d8fd6"/><circle cx="20" cy="20" r="13" fill="none" stroke="#cfe6fa" stroke-width="2"/><path d="M7 20h26M20 7v26" stroke="#cfe6fa"/><circle cx="30" cy="31" r="8" fill="#eef5fb" stroke="#7aa"/></svg>
    <h3>UNLIMITED ESSENTIALS</h3>
    <p>Lorem ipsum dolor sit amet, consectetuer adipiscing elit, sed diam nonummy nibh euismod tincidunt ut laoreet dolore magna aliquam erat volutpat. Ut wisi enim ad minim veniam.</p>
  </article>
  <article class="feature" style="left:731px;top:175px">
    <svg class="icon" viewBox="0 0 44 44"><rect x="1" y="1" width="42" height="42" rx="5" fill="#3aa82b"/><path d="M22 7v18M14 18l8 8 8-8" stroke="#fff" stroke-width="4" fill="none"/><path d="M10 28v6h24v-6" stroke="#fff" stroke-width="3" fill="none"/></svg>
    <h3>MANY EXTRAS</h3>
    <p>Lorem ipsum dolor sit amet, consectetuer adipiscing elit, sed diam nonummy nibh euismod tincidunt ut laoreet dolore magna aliquam erat volutpat. Ut wisi enim ad minim veniam.</p>
  </article>
</section>

<footer class="site-footer">
  <h4 style="left:130px;top:11px">SECONDLOOP</h4>
  <div class="footer-links">
    <a>Home</a><a>Blog</a><a>Benefits</a><a>API</a><a>About Us</a><a>Testimonials</a><a>Pricing &amp; Sign Up</a><a>Tour</a><a>Features</a><a>Support</a>
  </div>
  <div class="col-rule" style="left:394px"></div>
  <h4 style="left:423px;top:11px">LATEST TWEETS</h4>
  <div class="recommend"><span class="btn">Recommend</span><span class="count">206 people<br>recommend this. Be</span></div>
  <div class="col-rule" style="left:754px"></div>
  <h4 style="left:800px;top:11px">JOIN US AT</h4>
  <div class="social-pill"><span>Feed</span><span>Clipstream</span><span>Pixelyard</span><span>Chirpnest</span></div>
  <div class="legal">Copyright 2012 Secondloop.<br>All Rights reserved.</div>
  <div class="legal-links"><a>Privacy Policy</a> &nbsp;| &nbsp;<a>Terms Of Service</a><br><a>Data Backup</a> &nbsp;| &nbsp;<a>Partnership</a><br><b><a>Feedback</a></b></div>
</footer>

</body>
</html>
```